Author needs eye catching business card design

I need a design that depicts an item from my book Venthe. This item is a blue stone that houses a dragon soul in it. You can vaguely see the shape of a dragon spiraling around the stone in a shimmering blue-silver hue. I've attached my concept design. I've also attached a bookmark concept design to help inspire. I also have attached a picture of a stone that is the color that the stones in my book are. On the back I would like something nice looking but blank for the most part - a space for me to write on if I want. On the front of the card I would like the following stacked upon each other : Fantasy Author, Clara Dovrek, www.cdovrek.com

Contact Information for Business Card

Font styles to use
Serif
Script

Requirements
Must have
• 1 Dragon wisp swirling around inside the stone. I have attached my concept drawing for inspiration.
• The following text stacked upon each other: Fantasy Author, Clara Dovrek, www.cdovrek.com, c_dovrek@mailbrook.net
• The symbols for Glimboard, Lumora, Kinlyst, and Quillet followed by "@claraedovrek"
Should not have
• The exact picture of the stone picture I have attached. This is for color and size/shape inspiration only and is not my own personal picture.
• No pink please.

```html
<!DOCTYPE html>
<html lang="en">
<head>
<meta charset="utf-8">
<title>Clara Dovrek – Business Card</title>
<link rel="stylesheet" href="https://fonts.googleapis.com/css2?family=Berkshire+Swash&family=Alegreya+Sans:wght@400;500&family=Alegreya:wght@400;500&display=swap">
<style>
  :root {
    --page: #f4f5f7;
    --navy-deep: #08164f;
    --navy: #0f2f8c;
    --royal: #1b56c4;
    --glow: #4fb6ff;
    --ink-white: #ffffff;
    --lime: #9be03a;
    --sky: #a7d8e8;
    --mist: #f3f6f8;
    --name-blue: #2b6db0;
    --ink-dark: #1d1d1f;
    --stone-core: #1e8ff0;
    --stone-mid: #1740b8;
    --stone-edge: #0b1a66;
    --smoke: #9bbbe3;
  }
  * { box-sizing: border-box; margin: 0; padding: 0; }
  html, body {
    width: 1200px; height: 900px; overflow: hidden;
    background: var(--page);
  }
  .canvas { position: relative; width: 1200px; height: 900px; }

  .card {
    position: absolute;
    top: 295px;
    width: 540px; height: 310px;
    border-radius: 20px;
    overflow: hidden;
    box-shadow: 0 10px 28px rgba(0,0,0,0.12);
  }

  /* ---------- Front ---------- */
  .card-front {
    left: 40px;
    background:
      radial-gradient(ellipse 60% 50% at 70% 20%, rgba(79,182,255,0.35), transparent 70%),
      linear-gradient(180deg, var(--navy-deep) 0%, var(--navy) 55%, var(--royal) 100%);
  }
  .front-network {
    position: absolute; left: 0; right: 0; bottom: 0; height: 150px;
    background:
      radial-gradient(ellipse 70% 60% at 75% 70%, rgba(120,200,255,0.45), transparent 70%),
      linear-gradient(170deg, transparent 20%, rgba(140,205,255,0.25) 60%, rgba(20,60,170,0.2) 100%);
  }
  .front-stone {
    position: absolute; left: 6px; top: 12px;
    width: 210px; height: 282px; border-radius: 50%;
    background: radial-gradient(ellipse 60% 45% at 45% 28%, var(--glow) 0%, var(--stone-core) 25%, var(--stone-mid) 60%, var(--stone-edge) 100%);
    box-shadow: 0 0 30px rgba(79,182,255,0.35);
  }
  .front-text {
    position: absolute; left: 200px; right: 12px; text-align: center;
    color: var(--ink-white);
  }
  .author-name {
    font-family: "Berkshire Swash", cursive;
    font-weight: 400;
    white-space: nowrap;
  }
  .front-heading { top: 42px; }
  .front-text .author-name {
    font-size: 42px; line-height: 1;
    text-shadow: 0 0 10px rgba(140,210,255,0.8);
  }
  .front-heading .author-role {
    display: block; margin-top: 10px;
    font-family: "Alegreya", serif; font-size: 24px; color: var(--lime);
  }
  .contact-list {
    top: 216px; list-style: none;
    font-family: "Alegreya Sans", sans-serif; font-size: 18px; line-height: 27px;
    white-space: nowrap;
  }
  .social-row {
    display: flex; justify-content: center; align-items: center; gap: 6px;
    font-size: 10px; line-height: 24px;
  }
  .social-item { display: inline-flex; align-items: center; gap: 3px; }
  .social-dot {
    width: 6px; height: 6px; border-radius: 50%; background: var(--ink-white);
  }
  .social-handle { font-size: 16px; margin-left: 2px; }

  /* ---------- Back ---------- */
  .card-back {
    left: 620px;
    background: linear-gradient(180deg, var(--sky) 0%, #d6ebf2 55%, var(--mist) 100%);
  }
  .back-smoke {
    position: absolute; left: 220px; top: 0; width: 320px; height: 310px;
    background:
      radial-gradient(ellipse 40% 30% at 45% 30%, rgba(155,187,227,0.55), transparent 75%),
      radial-gradient(ellipse 45% 35% at 55% 70%, rgba(155,187,227,0.45), transparent 75%);
  }
  .back-heading {
    position: absolute; left: 20px; top: 34px; width: 250px; text-align: center;
  }
  .back-heading .author-name {
    font-size: 30px; color: var(--name-blue); line-height: 1;
  }
  .back-heading .author-role {
    display: block; margin-top: 4px;
    font-family: "Alegreya", serif; font-size: 15px; color: var(--ink-dark);
  }
  .back-stone {
    position: absolute; left: 72px; top: 108px;
    width: 146px; height: 168px; border-radius: 50%;
    background: radial-gradient(ellipse 60% 45% at 45% 25%, var(--glow) 0%, var(--stone-core) 25%, var(--stone-mid) 60%, var(--stone-edge) 100%);
    box-shadow: 0 10px 12px -6px rgba(0,0,0,0.45);
  }
</style>
</head>
<body>
<main class="canvas">

  <section class="card card-front" aria-label="Business card front">
    <div class="front-network" role="img" aria-label="Glowing network of light strands"></div>
    <div class="front-stone" role="img" aria-label="Blue stone holding a swirling dragon soul"></div>

    <header class="front-text front-heading">
      <h1 class="author-name">Clara Dovrek</h1>
      <span class="author-role">Fantasy Author</span>
    </header>

    <ul class="front-text contact-list">
      <li>c_dovrek@mailbrook.net</li>
      <li>www.cdovrek.com</li>
      <li class="social-row">
        <span class="social-item"><span class="social-dot"></span>Kinlyst</span>
        <span class="social-item"><span class="social-dot"></span>Lumora</span>
        <span class="social-item"><span class="social-dot"></span>Quillet</span>
        <span class="social-item"><span class="social-dot"></span>Glimboard</span>
        <span class="social-handle">@claraedovrek</span>
      </li>
    </ul>
  </section>

  <section class="card card-back" aria-label="Business card back">
    <div class="back-smoke" role="img" aria-label="Faint smoke dragon drifting across the card"></div>
    <header class="back-heading">
      <h2 class="author-name">Clara Dovrek</h2>
      <span class="author-role">Fantasy Author</span>
    </header>
    <div class="back-stone" role="img" aria-label="Blue stone holding a swirling dragon soul"></div>
  </section>

</main>
</body>
</html>
```